Optometric Practice needs Initial Photoshop Mockup

We need a graphic design for the homepage of a website for an optometric practice that specializes in vision therapy.

Here's the link to the project folder on Stashvale. I've included photos, example sites, content and instructions.

https://www.stashvale.example/sh/kx7rm2wq8zn41d9/BBQ_LmTyRwoPvXe3NcDrKuWjz

Please feel free to submit any questions about the design. I'll be happy to help guide you in any areas you're uncertain of.

Okay - I've updated the project to payment confirmed. Let's see some designs :) Thanks, Reg

```html
<!DOCTYPE html>
<html lang="en">
<head>
<meta charset="utf-8">
<title>Clearline Vision Learning Centers</title>
<link href="https://fonts.googleapis.com/css2?family=Mulish:ital,wght@0,400;0,600;0,700;1,400&display=swap" rel="stylesheet">
<style>
:root{
  --navy:#0b0b6f;
  --red:#9a1212;
  --text:#666;
  --dark:#333;
  --line:#d8d8d8;
  --foot:#efefef;
}
*{box-sizing:border-box;margin:0;padding:0}
html,body{width:866px;height:1200px;overflow:hidden;background:#fff;font-family:"Mulish",sans-serif;color:var(--text)}
.page{position:relative;width:866px;height:1200px;border-top:3px solid var(--red)}
.abs{position:absolute}
.brand{left:53px;top:22px}
.brand-name{display:flex;align-items:center;gap:7px;font-size:26px;font-weight:700;color:var(--navy);letter-spacing:2px}
.brand-name i{display:block;width:12px;height:12px;background:var(--red)}
.brand-sub{font-size:7px;color:var(--navy);margin-top:3px}
.brand-doc{font-size:10px;color:var(--navy);margin-top:18px}
.nav{left:0;top:98px;width:866px;height:33px;background:var(--navy);display:flex;padding-left:53px}
.nav a{color:#fff;font-size:9px;text-decoration:none;padding:0 8px;line-height:33px}
.nav a.active{background:var(--red)}
.hero{left:53px;top:137px;width:761px;height:276px;border:1px solid #ccc;box-shadow:0 1px 3px rgba(0,0,0,.15);padding:5px}
.hero-photo{position:relative;width:749px;height:265px;background:linear-gradient(90deg,#c48a6a 0%,#e64a4a 28%,#b86b52 45%,#7a5b4e 65%,#a3743e 82%,#6b5a4a 100%)}
.hero-copy{position:absolute;left:387px;top:82px;width:330px}
.hero-copy h2{font-weight:400;font-size:20px;color:#fff;letter-spacing:.3px}
.hero-copy p{font-size:12px;color:#222;line-height:18px;margin-top:14px}
.btn{display:inline-block;background:var(--navy);color:#fff;font-size:10px;text-decoration:none;text-transform:uppercase}
.hero-copy .btn{margin-top:14px;padding:8px 13px;border:1px solid #3a3ab0}
.dots{position:absolute;left:350px;top:245px;display:flex;gap:4px}
.dots span{width:9px;height:9px;background:#fff}
.dots span:first-child{background:var(--red)}
.side{left:53px;top:451px;width:239px}
.child-ad{height:114px;background:linear-gradient(90deg,#e6d6c6 0%,#d9c3ae 35%,#d5d5d8 60%,#c9c9ce 100%);border:1px solid #ccc;position:relative}
.child-ad p{position:absolute;left:109px;top:30px;color:var(--navy);font-size:11px}
.child-ad strong{display:block;font-weight:400;color:var(--red);font-size:19px;letter-spacing:1px;margin-top:3px}
.child-ad em{display:block;font-style:normal;font-size:13px;letter-spacing:3px;margin-top:2px}
.badge{margin-top:16px;height:36px;background:linear-gradient(#f2f2f2,#d9d9d9);border:1px solid #bbb}
.social-box{margin-top:16px;height:181px;border:1px solid #bbb;margin-left:2px}
.social-box h4{font-size:7px;color:#333;background:#eef0f6;padding:4px 18px;border-bottom:1px solid #c5c9d8}
.fan{display:flex;gap:4px;padding:9px 17px 0}
.fan i{width:30px;height:30px;background:#b9a69a;display:block}
.fan b{display:block;font-size:7px;color:var(--navy);line-height:9px}
.fan small{display:inline-block;margin-top:2px;background:#3b5998;color:#fff;font-size:6px;padding:1px 4px}
.fan-count{font-size:6px;padding:8px 17px 0}
.grid{display:grid;grid-template-columns:repeat(6,29px);gap:2px;padding:5px 17px}
.grid i{height:29px;display:block;background:#a9a9a9}
.grid i:nth-child(3n){background:#c4b3a2}
.grid i:nth-child(4n){background:#d8d8e0}
.plugin{font-size:6px;color:#8b97b8;border-top:1px solid #ddd;margin:2px 15px 0;padding-top:5px}
.story{margin-top:16px;height:167px;border:1px solid #bbb;padding:13px 11px}
.story h3{font-weight:400;font-size:15px;color:var(--navy)}
.story blockquote{font-style:italic;font-size:8.5px;line-height:15.5px;margin-top:10px}
.story blockquote::before{content:"\201C\201C";color:#ccc;font-size:22px;font-style:normal;line-height:0;vertical-align:-6px;margin-right:4px}
.story cite{display:block;font-style:normal;color:var(--red);font-size:8.5px;margin-top:6px}
.story a{display:block;margin-top:20px;color:var(--navy);font-size:8.5px}
.main{left:313px;top:448px;width:500px}
.welcome{font-weight:400;font-size:15px;color:var(--navy);line-height:18px}
.welcome span{display:block;color:var(--red);font-size:14px}
.main p{font-size:9px;line-height:16.8px;margin-top:7px}
.main p a{color:var(--red);text-decoration:none}
.provide{font-weight:400;font-size:15px;color:var(--navy);margin-top:12px}
.ticks{list-style:none;margin-top:6px}
.ticks li{position:relative;font-size:9px;line-height:15.5px;padding-left:17px;margin-bottom:8px}
.ticks svg{position:absolute;left:0;top:3px}
.main .btn{margin-top:4px;padding:8px 28px}
.rule{border-top:1px solid var(--line);margin-top:12px}
.news{font-weight:400;font-size:13.5px;color:var(--red);line-height:22px;margin-top:14px}
.main .news-p{line-height:15.5px;margin-top:10px}
.footer{left:0;top:1016px;width:866px;height:184px;background:linear-gradient(#e9e9e9,#f6f6f6)}
.f-brand{left:53px;top:30px}
.f-icons{left:53px;top:101px;display:flex;gap:6px}
.f-icons i{display:block;width:20px;height:20px;background:#8a8fb8;border-radius:3px}
.copy{left:53px;top:137px;font-size:8.5px;line-height:17px}
.copy b{font-weight:400;color:var(--red)}
.f-head{font-weight:400;font-size:11.5px;color:var(--red)}
.contact{left:248px;top:29px;width:380px}
.addr{display:flex;gap:30px;margin-top:10px}
.addr div{width:165px;font-size:8.5px;line-height:16.5px}
.addr h5{font-weight:400;font-size:10.5px;color:var(--navy);line-height:14px}
.addr .org{color:#444}
.phone{color:var(--red)}
.browse{left:638px;top:29px;width:190px}
.links{display:grid;grid-template-columns:120px 70px;grid-auto-flow:column;grid-template-rows:repeat(6,18.6px);margin-top:10px;font-size:8.5px;color:#555}
</style>
</head>
<body>
<div class="page">

  <header class="abs brand">
    <div class="brand-name"><i></i>CVLC</div>
    <div class="brand-sub">Clearline Vision Learning Centers, Inc.</div>
    <div class="brand-doc">Dr. Daniel Ferrow</div>
  </header>

  <nav class="abs nav">
    <a class="active" href="#">HOME</a><a href="#">MEET US</a><a href="#">NEW PATIENTS</a><a href="#">VISION &amp; LEARNING</a><a href="#">VISION THERAPY</a><a href="#">BINOCULAR VISION DISORDERS</a><a href="#">HEAD INJURIES</a><a href="#">PROFESSIONALS</a><a href="#">CONTACT US</a>
  </nav>

  <section class="abs hero">
    <div class="hero-photo" role="img" aria-label="Smiling young woman in a red top resting her chin on her hand in front of library bookshelves">
      <div class="hero-copy">
        <h2>IMPROVE YOUR VISION AT ANY AGE</h2>
        <p>Aenean a nibh eget turpis vehicula tempus ac sed massa. Vestibulum dolor nulla, ultrices ac tincidunt sed, laoreet non est.</p>
        <a class="btn" href="#">READ MORE ››</a>
      </div>
      <div class="dots"><span></span><span></span><span></span><span></span></div>
    </div>
  </section>

  <aside class="abs side">
    <div class="child-ad" role="img" aria-label="Young boy wearing glasses in front of an eye chart">
      <p>Does my child have a<strong>VISION</strong><em>PROBLEM?</em></p>
    </div>
    <div class="badge" role="img" aria-label="Patient reviews badge"></div>
    <div class="social-box">
      <h4>Find us on Friendlink</h4>
      <div class="fan"><i role="img" aria-label="Profile photo"></i><div><b>CVLC: Dr. Daniel Ferrow,<br>Developmental Optometrist</b><small>Like</small></div></div>
      <div class="fan-count">155 people like CVLC: Dr. Daniel Ferrow, Developmental Optometrist.</div>
      <div class="grid" role="img" aria-label="Follower profile photos"><i></i><i></i><i></i><i></i><i></i><i></i><i></i><i></i><i></i><i></i><i></i><i></i></div>
      <div class="plugin">Friendlink social plugin</div>
    </div>
    <div class="story">
      <h3>SUCCESS STORY</h3>
      <blockquote>Aliquam molestie, mi et imperdiet euismod, dui purus auctor tellus, et interdum lacus lectus et ante. Sed accumsan sollicitudin sapien, sit amet adipiscing turpis gravida ac. ..</blockquote>
      <cite>The C Family, Child's Age 6</cite>
      <a href="#">SUCCESS WITH VISION THERAPY ››</a>
    </div>
  </aside>

  <main class="abs main">
    <h1 class="welcome">WELCOME TO<span>CLEARLINE VISION LEARNING CENTERS, INC.</span></h1>
    <p>There are many visual skills critical for reading and learning. Often, a vision problem is misdiagnosed as an attention problem or a learning disability due to similarity of symptoms. Anyone who is struggling with reading, has poor reading comprehension, or just isn't performing to their full potential, should consider scheduling a developmental vision evaluation. To help determine if you or your child should be tested, <a href="#">Do the Checklist</a> on our <a href="#">Vision Quiz page.</a></p>
    <h2 class="provide">Clearline Vision Learning Centers and Dr. Daniel Ferrow provide:</h2>
    <ul class="ticks">
      <li><svg width="10" height="9" viewBox="0 0 10 9"><path d="M1 5l3 3 5-7" fill="none" stroke="#0b0b6f" stroke-width="2"/></svg>Comprehensive Eye Examinations for All Ages, including Infants and Preschoolers</li>
      <li><svg width="10" height="9" viewBox="0 0 10 9"><path d="M1 5l3 3 5-7" fill="none" stroke="#0b0b6f" stroke-width="2"/></svg>Vision Therapy for All Ages</li>
      <li><svg width="10" height="9" viewBox="0 0 10 9"><path d="M1 5l3 3 5-7" fill="none" stroke="#0b0b6f" stroke-width="2"/></svg>Treatment for Learning-related Vision Problems</li>
      <li><svg width="10" height="9" viewBox="0 0 10 9"><path d="M1 5l3 3 5-7" fill="none" stroke="#0b0b6f" stroke-width="2"/></svg>Free Monthly Seminars. Visit our Friendlink page for information about our free monthly seminars on a variety of topics, including: The Hidden Disability - Undiagnosed Vision Problems.</li>
      <li><svg width="10" height="9" viewBox="0 0 10 9"><path d="M1 5l3 3 5-7" fill="none" stroke="#0b0b6f" stroke-width="2"/></svg>Continuing Education seminars for Optometrists, Occupational Therapists and Physical Therapists. All CE offerings are free and board approved. For CE information and dates, see our success stories, blogs and videos on Binocular Vision Disorders.</li>
    </ul>
    <a class="btn" href="#">LEARN MORE ABOUT US</a>
    <div class="rule"></div>
    <h2 class="news">EYE-OPENING WORK: DOCTOR HELPS TO GET CHILDREN'S BRAINS TO COMMUNICATE WITH THEIR EYES</h2>
    <p class="news-p">BROOKFIELD, Md. (WKLT) — A doctor in Brookfield says there are children who have been labeled as lazy or hyper or learning deficient who are none of those things. As Ned Harlow reports, they have a simple problem getting their brain to communicate with their eyes. After getting two Ds in school, Mara Linden's mother brought her to see Dr. Daniel Ferrow.</p>
    <p class="news-p" style="margin-top:14px">The goal was to see what her brain was doing and what her eyes were seeing. All her life, Linden couldn't comprehend the words she read. Her eyes weren't working together. She saw double and couldn't track a line of words on the page.</p>
  </main>

  <footer class="abs footer">
    <div class="abs f-brand">
      <div class="brand-name"><i></i>CVLC</div>
      <div class="brand-sub">Clearline Vision Learning Centers, Inc.</div>
    </div>
    <div class="abs f-icons"><i></i><i></i><i></i><i></i></div>
    <div class="abs copy">Copyright © 2014. <b>CVLC.</b> All Right Reserved<br>Privacy Policy</div>
    <div class="abs contact">
      <h4 class="f-head">CONTACT INFORMATION</h4>
      <div class="addr">
        <div><h5>Clearline Vision Learning Centers</h5><span class="org">Dr. Daniel Ferrow</span><br>4410 Harrow Park Rd.<br>Linden Court, Ste. 3<br>Brookfield, MD, 21990<br><span class="phone">Phone: 555-014-2280 | Fax: 555-014-2291</span></div>
        <div><h5>Clearline Vision Learning Centers</h5><span class="org">Dr. Daniel Ferrow</span><br>72 Orchard Ave. Suite 200, Room 3<br>Eastmere, MD, 21997</div>
      </div>
    </div>
    <div class="abs browse">
      <h4 class="f-head">BROWSE OUR SITE</h4>
      <div class="links"><span>Home</span><span>Meet Us</span><span>New Patients</span><span>Vision &amp; Learning</span><span>Vision Therapy</span><span>Binocular Vision Disorders</span><span>Head Injuries</span><span>Professionals</span><span>Contact Us</span></div>
    </div>
  </footer>

</div>
</body>
</html>
```